HARBORLINE BANK Stationery and BRAND ARCHITECTURE

We need a unique Design and Architecture for:

a. Business Card
b. Letterhead
c. Continuation Sheet
d. Envelope
e. Email Signature
f. Complimentary Slip
g. Poster
h. Corporate Folder

1. Information for the call card:

Marcus J. Okafor
Senior Assistant Managing Director
General Banking Division
Harborline Bank
P.O. Box 517, Palmetto Lane, Basseterre, St. Kitts, West Indies
Office.: (869) 555-0148 Ext 2207
M.: (869) 555-0193
F.: (869) 555-0176
Email: marcusokafor@harborlinebankexample.com
harborlinebank.example

2. All pieces must include:
a. Address
b. Contact info
c.twitter and Facebook address

The Information for the posters:
Visual:A Happy Black Family
Headline Our future together – Better!
Bold Our People know how to build for the long term. How to root the future firmly in the strengths of our people.
A Harbor we can lean on for the better!

Target Market(s)

BUSiness
Bank Customers

Industry/Entity Type

Bank

Requirements
Must have
• - Logo wiht tag
• - use of Logo Colours
• - Green and Red as main colours but the yellow and black are also important
• - the red circles MUSt be used inthe brand architecture

```html
<!DOCTYPE html>
<html lang="en">
<head>
<meta charset="utf-8">
<title>Harborline Bank – Our Future Together Better</title>
<link href="https://fonts.googleapis.com/css2?family=Source+Sans+3:ital,wght@0,400;0,600;0,700;1,600;1,700&display=swap" rel="stylesheet">
<style>
  :root {
    --green: #1b6232;
    --red: #d42a2f;
    --yellow: #f6c418;
    --ink: #1e1e1e;
    --grey-text: #676767;
    --paper: #fbf1f2;
    --panel: #f1f1f3;
    --social-a: #3b5a9a;
    --social-b: #2aa3e0;
  }
  * { margin: 0; padding: 0; box-sizing: border-box; }
  html, body { width: 848px; height: 1200px; overflow: hidden; background: #fff; }
  .poster {
    position: relative;
    width: 848px;
    height: 1200px;
    overflow: hidden;
    background: var(--paper);
    font-family: "Source Sans 3", "Myriad Pro", sans-serif;
  }
  .poster__frame { position: absolute; inset: 0; }
  .brand { position: absolute; left: 32px; top: 32px; width: 330px; }
  .brand__mark {
    position: absolute; left: 94px; top: 0;
    width: 30px; height: 30px; border-radius: 50%;
    background: var(--red);
  }
  .brand__name {
    position: absolute; left: 0; top: 62px;
    font-weight: 700; font-size: 45px; line-height: 1;
    color: var(--green); letter-spacing: -0.5px; white-space: nowrap;
  }
  .brand__tag {
    position: absolute; left: 68px; top: 114px;
    font-weight: 600; font-size: 21px; line-height: 1;
    color: var(--ink); white-space: nowrap;
  }
  .headline {
    position: absolute; right: 32px; top: 122px;
    text-align: right; font-weight: 700;
    font-size: 86px; line-height: 83px; letter-spacing: -0.5px;
  }
  .headline span { display: block; }
  .headline .c-green { color: var(--green); }
  .headline .c-yellow { color: var(--yellow); }
  .headline .c-red { color: var(--red); }
  .message {
    position: absolute; right: 32px; top: 472px;
    text-align: right; font-style: italic; font-weight: 600;
    font-size: 35px; line-height: 38px; color: var(--grey-text);
    white-space: nowrap;
  }
  .message strong { font-weight: 700; }
  .slogan {
    position: absolute; right: 30px; top: 600px;
    font-weight: 600; font-size: 38px; line-height: 1;
    color: var(--red); white-space: nowrap;
  }
  .contact {
    position: absolute; right: 28px; top: 655px;
    text-align: right; font-size: 21.5px; line-height: 27.5px;
    font-style: normal;
    color: var(--ink); white-space: nowrap;
  }
  .social { position: absolute; left: 699px; top: 756px; display: flex; gap: 2px; }
  .social__item { width: 58px; height: 58px; border-radius: 50%; }
  .social__item--a { background: var(--social-a); }
  .social__item--b { background: var(--social-b); }
</style>
</head>
<body>
<main class="poster">
  <svg class="poster__frame" width="848" height="1200" viewBox="0 0 848 1200">
    <defs>
      <clipPath id="panel-clip">
        <ellipse cx="960" cy="860" rx="935" ry="820"/>
      </clipPath>
      <linearGradient id="family-tones" x1="0" y1="0" x2="1" y2="1">
        <stop offset="0" stop-color="#eceae8"/>
        <stop offset="0.45" stop-color="#9a6a4c"/>
        <stop offset="1" stop-color="#5b3a28"/>
      </linearGradient>
    </defs>
    <ellipse cx="960" cy="860" rx="935" ry="820" fill="var(--panel)"/>
    <g clip-path="url(#panel-clip)">
      <rect x="0" y="742" width="848" height="458" fill="url(#family-tones)" role="img" aria-label="Photo of a happy Black family: father, mother and two children smiling together"/>
    </g>
    <ellipse cx="960" cy="860" rx="935" ry="820" fill="none" stroke="var(--green)" stroke-width="38"/>
  </svg>

  <header class="brand">
    <span class="brand__mark"></span>
    <span class="brand__name">Harborline Bank</span>
    <span class="brand__tag">Anchored In Better</span>
  </header>

  <h1 class="headline">
    <span class="c-green">OUR</span>
    <span class="c-yellow">FUTURE</span>
    <span class="c-green">TOGETHER</span>
    <span class="c-red">BETTER!</span>
  </h1>

  <p class="message"><strong>Bold</strong> Our People know how to build for the<br>long term. How to root the future firmly in<br>the strengths of our people.</p>

  <p class="slogan">A Harbor we can lean on for the better!</p>

  <address class="contact">
    P: (869) 555-0148 Ext 2207 M: (869) 555-0193 E: (869) 555-0176<br>
    marcusokafor@harborlinebankexample.com | www.harborlinebank.example<br>
    P.O. Box 517, Palmetto Lane, Basseterre, St. Kitts, West Indies
  </address>

  <div class="social" aria-label="Social media links">
    <span class="social__item social__item--a" role="img" aria-label="Social media link one"></span>
    <span class="social__item social__item--b" role="img" aria-label="Social media link two"></span>
  </div>
</main>
</body>
</html>
```